Stanbrook Fire Services Pty Ltd

We need business cards for a company based in Perth, we install, service and maintain fire equipment.
On the front we want a great design with our logo and a small spot for our full company name, general company email address and office number. On the back we need space for our name, title, mobile number and email address on the back.

Target Market(s)

Facility managers and commercial/industrial building owners/occupiers.

Contact Information for Business Card

Font styles to use
Sans Serif

Requirements
Must have
• Please only submit 5 of your best samples.
Darker tones are preferred.
Nice to have
• We want to use, black, red and grey. Keep it modern and clean.
I've attached the company logo and a sample of a boarder we use on our emergency plans.
Should not have
• No preference. Let the designer choose.

```html
<!DOCTYPE html>
<html lang="en">
<head>
<meta charset="utf-8">
<title>Stanbrook Fire Services – Business Card</title>
<link rel="stylesheet" href="https://fonts.googleapis.com/css2?family=Arimo:wght@400;700&family=Bebas+Neue&family=Work+Sans:wght@400&display=swap">
<style>
  :root {
    --backdrop: #434343;
    --card-white: #ffffff;
    --brand-red: #ed1c24;
    --ink-black: #231f20;
    --text-dark: #2b2b2b;
    --shadow: rgba(20, 20, 20, 0.75);
  }
  * { margin: 0; padding: 0; box-sizing: border-box; }
  html, body {
    width: 1013px;
    height: 1200px;
    overflow: hidden;
    background: var(--backdrop);
  }
  .canvas { position: relative; width: 1013px; height: 1200px; }

  .card {
    position: absolute;
    left: 211px;
    width: 591px;
    height: 338px;
    box-shadow: 14px 16px 10px var(--shadow);
    overflow: hidden;
  }

  /* Personal side */
  .card--personal { top: 237px; background: var(--card-white); }
  .person {
    position: absolute;
    right: calc(591px - 262px);
    top: 136px;
    text-align: right;
  }
  .person__name {
    font-family: "Bebas Neue", "Oswald", sans-serif;
    color: var(--brand-red);
    font-size: 30px;
    line-height: 1;
    letter-spacing: 0.2px;
  }
  .person__title {
    font-family: "Work Sans", sans-serif;
    color: var(--text-dark);
    font-size: 15px;
    margin-top: 2px;
  }
  .divider {
    position: absolute;
    left: 295px;
    top: 101px;
    width: 1px;
    height: 122px;
    background: var(--brand-red);
  }
  .contact-list {
    position: absolute;
    left: 326px;
    top: 143px;
    list-style: none;
    font-family: "Work Sans", sans-serif;
    font-size: 15.5px;
    color: var(--text-dark);
  }
  .contact-list li { display: flex; align-items: center; height: 19px; }
  .contact-list svg { width: 11px; height: 11px; margin-right: 8px; flex: none; }
  .band--black { position: absolute; left: 0; top: 303px; width: 100%; height: 8px; background: var(--ink-black); }
  .band--red { position: absolute; left: 0; top: 316px; width: 100%; height: 22px; background: var(--brand-red); }

  /* Brand side */
  .card--brand { top: 640px; background: var(--brand-red); color: var(--card-white); text-align: center; }
  .brand-mark {
    position: absolute;
    left: 0; right: 0;
    top: 88px;
    font-family: "Arimo", sans-serif;
    font-weight: 700;
    font-size: 44px;
    letter-spacing: 1px;
    line-height: 1;
  }
  .company-name {
    position: absolute;
    left: 0; right: 0;
    top: 190px;
    font-family: "Arimo", sans-serif;
    font-size: 31px;
    line-height: 1;
  }
  .web-row {
    position: absolute;
    left: 0; right: 0;
    top: 247px;
    display: flex;
    justify-content: center;
    align-items: center;
    gap: 5px;
    font-family: "Arimo", sans-serif;
    font-size: 18px;
    line-height: 1;
  }
  .rule { height: 1.5px; width: 66px; }
  .rule--left { background: linear-gradient(to right, rgba(255,200,120,0), var(--card-white)); }
  .rule--right { background: linear-gradient(to left, rgba(255,200,120,0), var(--card-white)); }
  .phone-row {
    position: absolute;
    left: 0; right: 0;
    top: 281px;
    display: flex;
    justify-content: center;
    align-items: center;
    gap: 4px;
    font-family: "Arimo", sans-serif;
    font-size: 19px;
    line-height: 1;
  }
  .phone-row svg { width: 19px; height: 19px; }
</style>
</head>
<body>
<main class="canvas">

  <section class="card card--personal" aria-label="Personal contact side">
    <div class="person">
      <h1 class="person__name">Daniel Harper</h1>
      <p class="person__title">Manager</p>
    </div>
    <div class="divider"></div>
    <ul class="contact-list">
      <li>
        <svg viewBox="0 0 24 24" aria-hidden="true"><path fill="#ed1c24" d="M6.6 2.5l3 3.2-1.8 2.6c1.2 3 3.9 5.9 6.9 7.2l2.5-1.9 3.3 3-1.6 3.6C10.5 19.8 3.9 13 3.2 4.2z"/></svg>
        +61 412 587 903
      </li>
      <li>
        <svg viewBox="0 0 24 24" aria-hidden="true"><path fill="#ed1c24" d="M2 9l10-7 10 7v13H2zM4 10v1l8 6 8-6v-1l-8-5.5zM7 7h10v3l-5 3.5L7 10z"/></svg>
        danielharper@sfs.com
      </li>
    </ul>
    <div class="band--black"></div>
    <div class="band--red"></div>
  </section>

  <section class="card card--brand" aria-label="Company side">
    <p class="brand-mark">STANBROOK</p>
    <h2 class="company-name">Stanbrook Fire Services Pty Ltd</h2>
    <p class="web-row">
      <span class="rule rule--left"></span>
      www.stanbrookfireservices.com
      <span class="rule rule--right"></span>
    </p>
    <p class="phone-row">
      <svg viewBox="0 0 24 24" aria-hidden="true">
        <circle cx="12" cy="12" r="10.5" fill="none" stroke="#fff" stroke-width="1.8"/>
        <path fill="none" stroke="#fff" stroke-width="1.8" stroke-linejoin="round" d="M8.6 6.5l1.8 2.2-1 1.5c.7 1.8 2.2 3.3 4 4l1.5-1 2.2 1.8-1 2.3c-4.2-.4-7.9-4.1-8.3-8.3z"/>
      </svg>
      +0894001275
    </p>
  </section>

</main>
</body>
</html>
```